Real Estate Company / Capital Needs Cards!

need business cards designed using the logos that were just designed by sketchhive.

Reason: per designers request deadline extended 1 day…thank you.

Target Market(s)

Investors and clients looking to purchase real estate or invest in the business.

Industry/Entity Type

Business

Requirements
Must have
• two designs - one for the real estate logo and one for the capital logo, similar but slightly different.
Nice to have
• something to make it pop (perhaps on the back)
Should not have
• much color

```html
<!DOCTYPE html>
<html lang="en">
<head>
<meta charset="utf-8">
<title>Veranne Business Cards</title>
<link href="https://fonts.googleapis.com/css2?family=Cormorant+Garamond:wght@400;500&display=swap" rel="stylesheet">
<style>
  :root {
    --canvas: #ebe8e3;
    --card-black: #121212;
    --card-black-edge: #262626;
    --ink-light: #e9e6df;
    --ink-muted: #a9a59c;
    --cream: #e4dcc4;
    --cream-deep: #c9bd9a;
    --silver: #dcdcdc;
    --silver-deep: #a9a9a9;
    --serif: "Cormorant Garamond", Georgia, serif;
  }
  * { box-sizing: border-box; margin: 0; padding: 0; }
  html, body { width: 703px; height: 1200px; overflow: hidden; }
  body { background: var(--canvas); font-family: var(--serif); position: relative; }

  .card-set { position: absolute; left: 0; width: 703px; height: 600px; }
  .card-set--capital { top: 0; }
  .card-set--estate { top: 600px; }

  .card {
    position: absolute; left: 131px; width: 440px; height: 252px;
    border-radius: 8px; overflow: hidden;
    background: radial-gradient(ellipse at 50% 40%, var(--card-black-edge), var(--card-black) 75%);
    box-shadow: 0 4px 14px rgba(0,0,0,.25);
  }
  .card--front { top: 36px; }
  .card--back { top: 312px; }

  .brand { display: flex; align-items: center; gap: 12px; color: var(--ink-light); }
  .brand__mark { width: 46px; height: 46px; background: var(--ink-light); }
  .brand__name { font-weight: 400; font-size: 30px; letter-spacing: 3px; line-height: 1; text-transform: uppercase; }
  .brand__name span { display: block; font-size: 15px; letter-spacing: 2.5px; margin-top: 4px; }

  .card--front .brand { position: absolute; left: 50%; top: 50%; transform: translate(-50%, -50%); }

  .card--back .brand { position: absolute; left: 26px; top: 24px; gap: 9px; }
  .card--back .brand__mark { width: 30px; height: 30px; }
  .card--back .brand__name { font-size: 19px; letter-spacing: 2px; }
  .card--back .brand__name span { font-size: 10px; letter-spacing: 1.6px; margin-top: 3px; }

  .contact-person { position: absolute; right: 28px; top: 30px; text-align: right; color: var(--ink-light); }
  .contact-person__name { font-size: 24px; font-weight: 400; }
  .contact-person__role { font-size: 12px; color: var(--ink-muted); letter-spacing: 1px; margin-top: 2px; }

  .contact-list { position: absolute; right: 28px; top: 100px; list-style: none; color: var(--ink-light); font-size: 12px; letter-spacing: .5px; }
  .contact-list li { display: flex; align-items: center; justify-content: flex-end; gap: 8px; height: 18px; }
  .contact-list li::after { content: ""; width: 8px; height: 8px; background: var(--ink-muted); }

  .card__wave { position: absolute; left: 0; bottom: 0; width: 440px; height: 110px; }
</style>
</head>
<body>

<section class="card-set card-set--capital">
  <div class="card card--front">
    <div class="brand">
      <div class="brand__mark"></div>
      <div class="brand__name">Veranne<span>Capital, LLC</span></div>
    </div>
  </div>

  <div class="card card--back">
    <div class="brand">
      <div class="brand__mark"></div>
      <div class="brand__name">Veranne<span>Capital, LLC</span></div>
    </div>
    <div class="contact-person">
      <div class="contact-person__name">Owen Hartley</div>
      <div class="contact-person__role">Managing Director</div>
    </div>
    <ul class="contact-list">
      <li>T 555 214 0193</li>
      <li>M 555 214 0187</li>
      <li>owen@veranne.co</li>
      <li>www.veranne.co</li>
    </ul>
    <svg class="card__wave" viewBox="0 0 440 110" preserveAspectRatio="none">
      <path d="M0 40 C90 10 170 100 300 80 C360 70 410 95 440 110 L0 110 Z" fill="var(--cream-deep)"/>
      <path d="M0 58 C100 30 180 110 300 96 C360 90 410 104 440 110 L0 110 Z" fill="var(--cream)"/>
    </svg>
  </div>
</section>

<section class="card-set card-set--estate">
  <div class="card card--front">
    <div class="brand">
      <div class="brand__mark"></div>
      <div class="brand__name">Veranne<span>Real Estate</span></div>
    </div>
  </div>

  <div class="card card--back">
    <div class="brand">
      <div class="brand__mark"></div>
      <div class="brand__name">Veranne<span>Real Estate</span></div>
    </div>
    <div class="contact-person">
      <div class="contact-person__name">Owen Hartley</div>
      <div class="contact-person__role">Managing Director</div>
    </div>
    <ul class="contact-list">
      <li>T 555 214 0193</li>
      <li>M 555 214 0187</li>
      <li>owen@veranne.co</li>
      <li>www.veranne.co</li>
    </ul>
    <svg class="card__wave" viewBox="0 0 440 110" preserveAspectRatio="none">
      <path d="M0 40 C90 10 170 100 300 80 C360 70 410 95 440 110 L0 110 Z" fill="var(--silver-deep)"/>
      <path d="M0 58 C100 30 180 110 300 96 C360 90 410 104 440 110 L0 110 Z" fill="var(--silver)"/>
    </svg>
  </div>
</section>

</body>
</html>
```